Holloway Kitset Furniture Assembly Service needs a new flyer design

Holloway Kitset is a mobile furniture assembly service, that assembles furniture for the customer at there home or business

We are looking for a new feel and look to the flyer that we display within furniture stores based in Perth Western Australia.
The design must stand out to the customers that will be buying flatpack furniture and may need help assembling there products, from a simple chair, to a complete office / home fit out.

Our customer target varys from 18year olds to pensioners, male and female, and disabled.

we already have a logo, but must incorperate the company slogan " You buy We build" and also the words" At a price you can afford".

looking forward to seeing something new and away from the normal dull rubish, want to set a new benchmark.

please feel free to look at my website for information www.hollowaykitset-demo.com.au or hollowaykitsetdemo
on facebook.

Sorry have altered the brief a little.

Will also be looking for a new wrap design for the company vans in the very near future.

Target Market(s)

women, builders, contractors, etc, people that dislike building flatpack furniture and are in need of help.

Industry/Entity Type

Business

Requirements
Must have
• if possisble to incorperate the colour scheme.website, facebook site, and( prices start from $10)

Must have my regestered tradmark stamp/mark
Should not have
• not cheesy or tackey

```html
<!DOCTYPE html>
<html lang="en">
<head>
<meta charset="utf-8">
<title>Holloway Kitset Furniture Assembly Service</title>
<link href="https://fonts.googleapis.com/css2?family=Arimo:wght@400;700&family=Roboto+Condensed:wght@700&family=Open+Sans:ital,wght@1,400;1,700&family=Dancing+Script:wght@700&display=swap" rel="stylesheet">
<style>
  :root {
    --bg-top: #e6d6b8;
    --bg-bottom: #efe6d6;
    --panel: #f3ece0;
    --white: #ffffff;
    --ink: #6a6464;
    --brown: #5d4a36;
    --brown-deep: #6b3f1e;
    --olive: #b9a42c;
    --rule: #222222;
    --slogan: #7d7772;
  }
  * { margin: 0; padding: 0; box-sizing: border-box; }
  html, body { width: 927px; height: 1200px; overflow: hidden; }
  body {
    position: relative;
    font-family: "Arimo", Arial, sans-serif;
    background: linear-gradient(180deg, var(--bg-top) 0%, #eadcc2 45%, var(--bg-bottom) 70%);
  }
  .abs { position: absolute; }

  .header {
    left: 29px; top: 40px; width: 870px; height: 170px;
    background: var(--white);
    border-bottom: 6px solid var(--rule);
  }
  .brand-mark {
    left: 62px; top: 62px; width: 46px; height: 46px;
    background: var(--olive);
  }
  .brand-name {
    left: 139px; top: 62px;
    font-weight: 700; font-size: 26px; line-height: 24px;
    color: var(--brown); text-transform: uppercase; letter-spacing: -0.5px;
  }
  .trademark { font-size: 12px; vertical-align: top; line-height: 12px; margin-left: 2px; }
  .slogan {
    left: 155px; top: 112px;
    font-weight: 700; font-size: 14px; line-height: 16px; color: var(--slogan);
  }
  .price-line {
    left: 131px; top: 130px;
    font-weight: 700; font-size: 14px; line-height: 16px; color: var(--slogan);
  }
  .header-photo {
    left: 451px; top: 16px; width: 240px; height: 148px;
    background: radial-gradient(ellipse at 60% 55%, #cfcfcf 0%, #e9e9e9 55%, #ffffff 80%);
  }
  .need-help {
    left: 661px; top: 78px;
    font-weight: 700; font-size: 29px; color: #6b5545;
  }

  .assemble-list {
    left: 146px; top: 226px;
    font-weight: 700; font-size: 17.5px; color: var(--white);
    letter-spacing: -0.3px; word-spacing: 2px;
    text-shadow: 0 0 2px #6b5a40, 1px 1px 1px #6b5a40;
    white-space: nowrap;
  }
  .assemble-list span { margin-left: 24px; }
  .and-more {
    left: 676px; top: 246px;
    font-family: "Dancing Script", cursive; font-size: 14px; color: var(--white);
    text-shadow: 0 0 2px #6b5a40;
  }
  .service-title {
    left: 270px; top: 249px;
    font-weight: 700; font-size: 29.5px; color: var(--white);
    text-shadow: 0 0 2px #4a3b2a, 1px 2px 2px #4a3b2a;
    white-space: nowrap;
  }

  .photo { box-shadow: 0 2px 6px rgba(0,0,0,0.35); border: 2px solid #f4efe6; }
  .photo-boxes { left: 32px; top: 346px; width: 100px; height: 120px;
    background: linear-gradient(135deg, #c9a679, #a5825a 60%, #e6e2dc); }
  .photo-fittings { left: 130px; top: 324px; width: 134px; height: 166px;
    background: linear-gradient(160deg, #d9d9d6, #b7a37f 55%, #3d3c3c); }
  .photo-main { left: 264px; top: 294px; width: 406px; height: 260px;
    background: linear-gradient(150deg, #d8c9b6 0%, #c98a45 45%, #d99a55 70%, #d7d1ca 100%); z-index: 2; }
  .photo-drill { left: 670px; top: 324px; width: 130px; height: 166px;
    background: linear-gradient(160deg, #e1a868, #c8773a 50%, #9b2a22); }
  .photo-table { left: 800px; top: 346px; width: 94px; height: 120px;
    background: linear-gradient(180deg, #9c8a70, #c69a5c 60%, #8e5d3a); }

  .tagline { color: var(--brown); font-weight: 700; font-size: 24px; white-space: nowrap; }
  .tagline em { font-style: normal; color: var(--olive); font-size: 35px; letter-spacing: -0.5px; }
  .tagline-1 { left: 200px; top: 562px; }
  .tagline-2 { left: 433px; top: 601px; }

  .info-panel {
    left: 29px; top: 654px; width: 872px; height: 524px;
    background: var(--panel);
    box-shadow: 0 0 4px rgba(0,0,0,0.15);
  }
  .info-card {
    left: 56px; top: 674px; width: 818px; height: 404px;
    background: var(--white);
    border: 1px solid #ddd3c3;
  }
  .info-text {
    font-weight: 700; font-size: 29.5px; line-height: 30.4px; color: var(--ink);
    letter-spacing: -0.3px; white-space: nowrap;
  }
  .info-text-1 { left: 86px; top: 700px; }
  .info-text-2 { left: 86px; top: 898px; }

  .price-tag {
    left: 652px; top: 665px; width: 238px; height: 221px;
    background: var(--olive);
    color: var(--white);
    text-align: center;
    font-family: "Roboto Condensed", "Arial Narrow", sans-serif;
    font-weight: 700;
    text-shadow: 1px 2px 2px rgba(60,45,10,0.55);
  }
  .price-tag .label { font-size: 27px; line-height: 38px; padding-top: 26px; }
  .price-tag .amount { font-size: 110px; line-height: 110px; letter-spacing: -6px; margin-top: -2px; }
  .price-fold { left: 874px; top: 886px; }

  .contact-bar {
    left: 56px; top: 1092px; width: 818px; height: 74px;
    background: var(--brown-deep);
    color: var(--white);
    font-family: "Open Sans", Arial, sans-serif; font-style: italic;
    text-align: center;
  }
  .contact-bar .lead { font-size: 19px; padding-top: 5px; line-height: 24px; }
  .contact-bar .details { font-weight: 700; font-size: 14.5px; line-height: 20px; white-space: nowrap; }
  .contact-bar .details span { margin: 0 9px; }
</style>
</head>
<body>

  <header class="abs header">
    <div class="abs brand-mark"></div>
    <div class="abs brand-name">Holloway<br>Kitset<span class="trademark">®</span></div>
    <div class="abs slogan">you buy we build</div>
    <div class="abs price-line">At a price you can afford</div>
    <div class="abs header-photo" role="img" aria-label="Photo of a woman sitting on the floor assembling flat pack furniture with a screwdriver"></div>
    <div class="abs need-help">need help?</div>
  </header>

  <div class="abs assemble-list">WE ASSEMBLE:<span style="margin-left:8px">COMPUTERDESKS</span><span>BEDROOM FURNITURE</span><span>KITCHEN</span></div>
  <div class="abs and-more">...and more</div>
  <h1 class="abs service-title">Furniture assembly service</h1>

  <div class="abs photo photo-boxes" role="img" aria-label="Photo of flat pack cardboard boxes leaning against a wall"></div>
  <div class="abs photo photo-fittings" role="img" aria-label="Photo of bags of screws and fittings on a board"></div>
  <div class="abs photo photo-drill" role="img" aria-label="Photo of a cordless drill on pine boards"></div>
  <div class="abs photo photo-table" role="img" aria-label="Photo of an assembled wooden table and chairs"></div>
  <div class="abs photo photo-main" role="img" aria-label="Photo of a man kneeling among pine boards reading assembly instructions"></div>

  <p class="abs tagline tagline-1">We take the <em>frustration</em></p>
  <p class="abs tagline tagline-2">out of <em>furniture</em> assembly!</p>

  <section class="abs info-panel"></section>
  <div class="abs info-card"></div>
  <p class="abs info-text info-text-1">Why spend your day struggling with the<br>assembly of your new flatpack furniture,<br>when one of our skilled technicians can<br>have your furniture assembled and in-<br>stalled in no time, without the hassel of<br>having to assemble the items yourself.</p>
  <p class="abs info-text info-text-2">We will always work around your schedule, with one<br>of our experienced technicians available when you<br>need them. Holloway Kitset is a furniture assembly<br>service that takes the frustration out furniture assem-<br>bly, at an affordable price.</p>

  <div class="abs price-tag">
    <div class="label">PRICES START<br>FROM</div>
    <div class="amount">$10</div>
  </div>
  <svg class="abs price-fold" width="16" height="16" viewBox="0 0 16 16" aria-hidden="true"><polygon points="0,0 16,0 0,16" fill="#3a3328"/></svg>

  <footer class="abs contact-bar">
    <div class="lead">For more information please contact:</div>
    <div class="details"><span>Tel: 0491570156</span><span>Email: info@hollowaykitsetdemo.com.au</span></div>
    <div class="details"><span>Web: www.hollowaykitset-demo.com.au</span><span>Facebook: hollowaykitsetdemo</span></div>
  </footer>

</body>
</html>
```